Harbor Crest Data Systems Needs a Website Desing

We need a website design for a new company based in Kuwait called Harbor Crest Data Systems (HCDS). We provide Software as a Service (SaaS) solutions for small and medium business companies. We will develop the required E-systems like HR,Payroll,Accounting Systems for those customers who wants to focus on their business instead of wasting time to automate it. HCDS need a web site that represent this activity and showing our cloud products and allow out customers to easily identify their needs. as a normal web site basic things need to be included like :
about HCDS
Solutions
PressRoom
Contact us
please i need something similar to trelvoxa.com or qup.com or www.dro7lak.com with blue and black theme .. please check the Company's logo
Updates
hi all ,,,
the project is only design without any codes
Reason: The project is focus on design only ,, i will be really appreciated to have more designs

```html
<!DOCTYPE html>
<html lang="en">
<head>
<meta charset="utf-8">
<title>Harbor Crest Data Systems</title>
<link href="https://fonts.googleapis.com/css2?family=Source+Sans+3:wght@300;400;600;700&family=PT+Sans+Narrow&display=swap" rel="stylesheet">
<style>
:root{
  --ink:#0d0d0d;
  --blue:#0a8fd0;
  --blue-deep:#0577b8;
  --blue-light:#4fb9e8;
  --sky-top:#1c5fd0;
  --sky-mid:#5aa2e6;
  --sky-low:#b8d8f2;
  --white:#ffffff;
  --footer:#f4f4f4;
  --rule:rgba(255,255,255,.35);
}
*{margin:0;padding:0;box-sizing:border-box}
html,body{width:1200px;height:1089px;overflow:hidden;background:var(--white)}
body{position:relative;font-family:"Source Sans 3",sans-serif;color:var(--ink)}
.site-header{position:absolute;left:0;top:0;width:1200px;height:72px;background:var(--white)}
.brand{position:absolute;left:157px;top:12px;display:flex;align-items:center;gap:8px}
.brand-dot{width:44px;height:44px;border-radius:50%;background:var(--blue-deep)}
.brand-name{font-size:40px;font-weight:700;color:var(--ink);line-height:1}
.search{position:absolute;left:870px;top:7px;width:171px;height:38px;border:1px solid #cfcfcf;border-radius:8px;background:linear-gradient(#fff,#f0f0f0);font-size:13px;color:#444;padding:14px 0 0 12px}
.search svg{position:absolute;right:8px;top:11px}
.main-nav{position:absolute;left:579px;top:54px;width:464px;height:35px;background:linear-gradient(#4a4a4a,#0c0c0c 60%,#000);border-radius:6px 6px 0 0;display:flex;box-shadow:0 3px 6px rgba(0,0,0,.35);z-index:2}
.main-nav a{flex:1;color:var(--white);text-decoration:none;font-family:"PT Sans Narrow",sans-serif;font-size:16px;text-align:center;line-height:35px;border-right:1px solid #333}
.main-nav a:last-child{border-right:none}
.hero{position:absolute;left:0;top:72px;width:1200px;height:500px;background:linear-gradient(160deg,var(--sky-top) 0%,var(--sky-mid) 45%,var(--sky-low) 100%)}
.hero-photo{position:absolute;left:0;top:0;width:560px;height:500px;background:linear-gradient(90deg,#c9b5a4 0%,#b9a391 55%,rgba(185,163,145,0) 100%)}
.hero-title{position:absolute;left:603px;top:450px;font-size:42px;font-weight:300;color:#1c2a3a;letter-spacing:-.5px}
.hero-arrows{position:absolute;left:974px;top:518px;display:flex;gap:6px}
.hero-shade{position:absolute;left:0;bottom:0;width:1200px;height:16px;background:linear-gradient(transparent,rgba(0,0,0,.45))}
.content{position:absolute;left:0;top:572px;width:1200px;height:439px;background:radial-gradient(ellipse at 50% 0%,var(--blue-light),var(--blue) 60%,var(--blue-deep) 100%);color:var(--white)}
.col{position:absolute;top:14px}
.col h2{font-size:27px;font-weight:300;margin-bottom:8px}
.col-solutions{left:157px;width:190px}
.solutions-image{width:189px;height:89px;background:linear-gradient(#f4f8fb,#d6e8f4);margin-bottom:8px}
.col p{font-size:13px;line-height:18.5px;text-align:justify}
.btn{display:flex;align-items:center;gap:10px;width:189px;height:40px;border-radius:7px;background:linear-gradient(#fff,#e4e4e4);color:#222;font-size:14px;padding-left:14px;margin-top:14px}
.btn strong{font-size:18px;font-weight:400;color:var(--blue-deep)}
.col-saas{left:390px;width:402px;border-left:1px solid var(--rule);padding-left:0}
.divider{position:absolute;top:24px;width:1px;height:416px;background:var(--rule)}
.col-saas h3{font-size:19px;font-weight:400;color:#0b2a3f;line-height:23px;margin:8px 0 6px 2px}
.col-saas p{margin-left:2px;margin-bottom:17px}
.get-more{display:inline-block;margin-left:4px;background:linear-gradient(#333,#000);color:var(--white);font-size:15px;padding:6px 10px;margin-top:-4px}
.col-press{left:834px;width:208px}
.press-item{padding:10px 0 10px 3px;border-bottom:1px dotted rgba(255,255,255,.7)}
.press-item:last-child{border-bottom:none}
.press-date{font-size:13px;color:#0b2a3f;margin-bottom:4px}
.press-item p{margin-bottom:4px}
.press-more{font-size:12px;color:#0b2a3f}
.site-footer{position:absolute;left:0;top:1011px;width:1200px;height:78px;background:var(--footer);font-size:11px;color:#222}
.follow{position:absolute;left:157px;top:8px}
.social{display:flex;gap:10px;margin-top:9px}
.social span{width:25px;height:25px;border-radius:50%}
.footer-links{position:absolute;right:157px;top:8px;text-align:right;line-height:19px}
</style>
</head>
<body>
<header class="site-header">
  <div class="brand"><span class="brand-dot"></span><span class="brand-name">HCDS</span></div>
  <div class="search">Search
    <svg width="16" height="16" viewBox="0 0 16 16"><circle cx="6" cy="6" r="4.5" fill="none" stroke="#333" stroke-width="1.6"/><line x1="9.5" y1="9.5" x2="14" y2="14" stroke="#333" stroke-width="2"/></svg>
  </div>
  <nav class="main-nav"><a>Home</a><a>About HCDS</a><a>Solutions</a><a>PressRoom</a><a>Contact Us</a></nav>
</header>

<section class="hero">
  <div class="hero-photo" role="img" aria-label="Photo of a man touching a transparent cloud interface screen against a blue sky"></div>
  <h1 class="hero-title">Cloud Computing Company</h1>
  <div class="hero-arrows">
    <svg width="34" height="34" viewBox="0 0 34 34"><circle cx="17" cy="17" r="16" fill="#2b2b2b" stroke="#888"/><polyline points="20,10 13,17 20,24" fill="none" stroke="#fff" stroke-width="3"/></svg>
    <svg width="34" height="34" viewBox="0 0 34 34"><circle cx="17" cy="17" r="16" fill="#2b2b2b" stroke="#888"/><polyline points="14,10 21,17 14,24" fill="none" stroke="#fff" stroke-width="3"/></svg>
  </div>
  <div class="hero-shade"></div>
</section>

<main class="content">
  <section class="col col-solutions">
    <h2>Solutions</h2>
    <div class="solutions-image" role="img" aria-label="Illustration of devices and servers connected by arrows to a central cloud"></div>
    <p>Vantrel to work with Marisbay Bank for global rollout of Ledgerwave: Cloud-based software as a service.</p>
    <div class="btn" style="margin-top:26px">
      <svg width="28" height="20" viewBox="0 0 28 20"><rect x="1" y="1" width="26" height="18" rx="2" fill="#2aa3dc"/><polyline points="1,1 14,11 27,1" fill="none" stroke="#fff" stroke-width="1.5"/></svg>
      <span>Contact For <strong>HCDS</strong></span>
    </div>
    <div class="btn">
      <svg width="28" height="28" viewBox="0 0 28 28"><rect x="0" y="0" width="28" height="28" rx="5" fill="#f08a24"/></svg>
      <span>Read <strong>HCDS</strong> Blog</span>
    </div>
  </section>

  <div class="divider" style="left:371px"></div>
  <section class="col col-saas" style="border-left:none">
    <h2>SaaS cloud</h2>
    <h3>Software as a service that lowers complexity and costs</h3>
    <p>More and more organizations of all sizes and types are turning to SaaS (software as a service) as an alternative to buying, installing and maintaining licensed software. Through SaaS, organizations avoid the costs—both direct and indirect—of managing their own software by subscribing to Web-hosted applications managed by software as a service providers. Key advantages of cloud software include money savings, faster software implementations and upgrades, and increased focus on mission-critical objectives.</p>
    <p>Vantrel is adapting its industry-leading IP-based applications, particularly in the financial, insurance and government sectors, to support the cloud-based software as a service model. Our LedgerwaveTM SaaS cloud-based platform, for example, delivers all the infrastructure, software and support resources necessary to power a bank's global trade business</p>
    <span class="get-more">GET MORE</span>
  </section>

  <div class="divider" style="left:816px"></div>
  <section class="col col-press">
    <h2>Press Room</h2>
    <div class="press-item"><div class="press-date">March 6, 2013</div><p>Using Vantrel's SecureGov Provisional Authority to Operate</p><span class="press-more">Read More &gt;&gt;</span></div>
    <div class="press-item"><div class="press-date">February 12, 2013</div><p>Observations from California's cloud computing forum.</p><span class="press-more">Read More &gt;&gt;</span></div>
    <div class="press-item"><div class="press-date">December 18, 2012</div><p>Moving to the cloud? Ready to let go?</p><span class="press-more">Read More &gt;&gt;</span></div>
  </section>
</main>

<footer class="site-footer">
  <div class="follow">Follow us On
    <div class="social"><span style="background:#2d5fa8"></span><span style="background:#3cb4e6"></span><span style="background:#f07a1e"></span></div>
  </div>
  <div class="footer-links">Home &nbsp;/&nbsp; About HCDS &nbsp;/&nbsp; Solutions &nbsp;/&nbsp; PressRoom &nbsp;/&nbsp; Contact us<br>Copyrights @ 2013 All Rights Reserved</div>
</footer>
</body>
</html>
```